Bref créative
Fun, professional business cards/advertisment for dog boarding kennel
Bright Meadow Dog Boarding
I need double sided standard sized Business Card [3.5" x 2"]
Papyrus (name) and cambria (other type)
Bright & Fun-filled
Renata & Gideon - Certified Dog Lovers
481 Palomar Lane
Yellowknife, NT
brightmeadow@pawmail.example
http://www.brightmeadowdogboarding.example
Daily, weekly, monthly dog boarding.
Multi-dog discounts
Doggie day camp and overnight boarding
Individualized care, affordable rates
Formally Furlough Pet Camp & Boarding
Call to schedule services today!
On the back of the business cards we would like it quite simple- just the logo with our website and (867) 555-0142
We would like the front to be able to be used as an advertisement....like made into a magnet, so on the front we would like our name, logo and small bullet points as noted in the other comments.
We would like a fun, happy, but simple appearance. Please keep the fonts the same as in the logo.
fonts to use
AI file of our logo as requested

```html
<!DOCTYPE html>
<html lang="en">
<head>
<meta charset="utf-8">
<title>Bright Meadow Dog Boarding – Stationery</title>
<link href="https://fonts.googleapis.com/css2?family=Caladea:wght@400;700&display=swap" rel="stylesheet">
<style>
  :root {
    --backdrop: #3a3a3c;
    --paper: #ffffff;
    --brand-blue: #2a6cb0;
    --brand-blue-dark: #1f5590;
    --accent-red: #d8343a;
    --ink: #2b2b2b;
    --ink-soft: #7a7a7a;
    --rule: #9aa7b5;
    --mark-tint: #e6edf5;
  }
  * { box-sizing: border-box; margin: 0; padding: 0; }
  html, body { width: 1200px; height: 698px; overflow: hidden; }
  body {
    background: var(--backdrop);
    font-family: "Caladea", Cambria, Georgia, serif;
    color: var(--ink);
    position: relative;
  }
  .sheet {
    position: absolute;
    background: var(--paper);
    overflow: hidden;
    box-shadow: 0 6px 18px rgba(0,0,0,.35);
  }
  .brand-name {
    font-family: "Caladea", Cambria, Georgia, serif;
    font-weight: 700;
    color: var(--brand-blue);
    line-height: 1.05;
    text-align: center;
  }
  .brand-dot {
    display: inline-block;
    border-radius: 50%;
    background: var(--brand-blue);
  }
  .mark-faint {
    position: absolute;
    border-radius: 50% 50% 0 0;
    background: radial-gradient(circle at 50% 60%, var(--mark-tint), rgba(230,237,245,0) 70%);
  }
  .band {
    position: absolute;
    left: 0; right: 0;
    background: var(--brand-blue);
    color: #fff;
    display: flex;
    align-items: center;
    justify-content: center;
    letter-spacing: .04em;
  }

  /* Compliments card */
  .compliments { left: 40px; top: 70px; width: 320px; height: 200px; }
  .compliments .logo { position: absolute; left: 22px; top: 20px; width: 120px; }
  .compliments .brand-name { font-size: 15px; text-align: left; }
  .compliments .brand-dot { width: 10px; height: 10px; margin-bottom: 4px; }
  .compliments .mark-faint { left: 110px; top: 60px; width: 150px; height: 110px; }
  .compliments .band { bottom: 0; height: 24px; font-size: 8px; }
  .compliments .band::before { content: ""; position: absolute; top: -5px; left: 0; right: 0; height: 3px; background: var(--brand-blue); }

  /* Business cards */
  .card { width: 220px; height: 126px; border-radius: 8px; }
  .card-back { left: 40px; top: 320px; }
  .card-back .logo { position: absolute; left: 0; right: 0; top: 22px; text-align: center; }
  .card-back .brand-name { font-size: 17px; }
  .card-back .brand-dot { width: 12px; height: 12px; margin-bottom: 4px; }
  .card-back .band { bottom: 0; height: 30px; flex-direction: column; font-size: 8px; gap: 2px; }

  .card-front { left: 40px; top: 474px; height: 140px; }
  .card-front .logo { position: absolute; left: 14px; top: 16px; width: 90px; }
  .card-front .brand-name { font-size: 12px; text-align: left; }
  .card-front .brand-dot { width: 9px; height: 9px; margin-bottom: 3px; }
  .card-front .people { position: absolute; right: 14px; top: 18px; text-align: right; }
  .card-front .people strong { display: block; color: var(--brand-blue); font-size: 11px; letter-spacing: .04em; }
  .card-front .people span { font-size: 8px; color: var(--ink-soft); }
  .card-front .contact { position: absolute; right: 14px; top: 58px; list-style: none; text-align: right; font-size: 7.5px; line-height: 1.6; }
  .card-front .contact li::after { content: ""; display: inline-block; width: 5px; height: 5px; margin-left: 5px; background: var(--accent-red); border-radius: 50%; }
  .card-front .band { bottom: 0; height: 20px; font-size: 7.5px; }

  /* Letterhead */
  .letterhead { left: 400px; top: 24px; width: 300px; height: 424px; }
  .letterhead .logo { position: absolute; left: 0; right: 0; top: 18px; text-align: center; }
  .letterhead .brand-name { font-size: 13px; }
  .letterhead .brand-dot { width: 10px; height: 10px; margin-bottom: 3px; }
  .letterhead .mark-faint { left: 60px; top: 230px; width: 180px; height: 140px; }
  .letterhead .band { bottom: 0; height: 30px; flex-direction: column; font-size: 7.5px; gap: 2px; }
  .letterhead .band::before { content: ""; position: absolute; top: -6px; left: 0; right: 0; height: 3px; background: var(--brand-blue); }

  /* Fax */
  .fax { left: 740px; top: 70px; width: 300px; height: 424px; }
  .fax .logo { position: absolute; right: 24px; top: 18px; width: 110px; }
  .fax .brand-name { font-size: 12px; }
  .fax .logo { text-align: center; }
  .fax .brand-dot { width: 9px; height: 9px; margin-bottom: 3px; }
  .fax .title { position: absolute; right: 24px; top: 78px; font-size: 18px; font-weight: 700; color: var(--ink); letter-spacing: .08em; }
  .fax-table { position: absolute; left: 24px; right: 24px; top: 106px; border-collapse: collapse; font-size: 8px; color: var(--ink-soft); }
  .fax-table td { border: 1px solid var(--rule); height: 18px; padding: 0 5px; }
  .fax-table td.label { width: 52px; color: var(--ink); }
  .fax .message { position: absolute; left: 24px; right: 24px; top: 228px; }
  .fax .message i { display: block; height: 1px; background: #e2e2e2; margin-bottom: 16px; }
  .fax .mark-faint { left: 60px; top: 250px; width: 180px; height: 130px; }
  .fax .band { bottom: 0; height: 30px; flex-direction: column; font-size: 7.5px; gap: 2px; }
  .fax .band::before { content: ""; position: absolute; top: -6px; left: 0; right: 0; height: 3px; background: var(--brand-blue); }

  /* Envelope */
  .envelope { left: 740px; top: 524px; width: 340px; height: 150px; }
  .envelope svg { position: absolute; inset: 0; }
  .envelope .logo { position: absolute; left: 0; right: 0; top: 90px; text-align: center; }
  .envelope .brand-name { font-size: 11px; }
  .envelope .brand-dot { width: 8px; height: 8px; margin-right: 4px; vertical-align: middle; }
</style>
</head>
<body>

  <section class="sheet compliments" aria-label="Compliments slip">
    <div class="logo"><span class="brand-dot"></span><div class="brand-name">Bright Meadow Dog Boarding</div></div>
    <div class="mark-faint" role="img" aria-label="Faint brand emblem decoration"></div>
    <div class="band">http://www.brightmeadowdogboarding.example</div>
  </section>

  <section class="sheet card card-back" aria-label="Business card back">
    <div class="logo"><span class="brand-dot"></span><div class="brand-name">Bright Meadow<br>Dog Boarding</div></div>
    <div class="band"><span>www.brightmeadowdogboarding.example</span><span>(867) 555-0142</span></div>
  </section>

  <section class="sheet card card-front" aria-label="Business card front">
    <div class="logo"><span class="brand-dot"></span><div class="brand-name">Bright Meadow Dog Boarding</div></div>
    <div class="people"><strong>RENATA &amp; GIDEON</strong><span>Certified Dog Lovers</span></div>
    <ul class="contact">
      <li>481 Palomar Lane, Yellowknife, NT</li>
      <li>(867) 555-0142</li>
      <li>brightmeadow@pawmail.example</li>
    </ul>
    <div class="band">www.brightmeadowdogboarding.example</div>
  </section>

  <section class="sheet letterhead" aria-label="Letterhead">
    <div class="logo"><span class="brand-dot"></span><div class="brand-name">Bright Meadow<br>Dog Boarding</div></div>
    <div class="mark-faint" role="img" aria-label="Faint brand emblem decoration"></div>
    <div class="band"><span>481 Palomar Lane, Yellowknife, NT · (867) 555-0142</span><span>http://www.brightmeadowdogboarding.example</span></div>
  </section>

  <section class="sheet fax" aria-label="Fax cover sheet">
    <div class="logo"><span class="brand-dot"></span><div class="brand-name">Bright Meadow<br>Dog Boarding</div></div>
    <div class="title">FAX</div>
    <table class="fax-table">
      <tr><td class="label">To:</td><td></td><td class="label">From:</td><td></td></tr>
      <tr><td class="label">Fax:</td><td></td><td class="label">Pages:</td><td></td></tr>
      <tr><td class="label">Phone:</td><td></td><td class="label">Date:</td><td></td></tr>
      <tr><td class="label">Re:</td><td colspan="3"></td></tr>
      <tr><td class="label">Notes:</td><td colspan="3"></td></tr>
    </table>
    <div class="message"><i></i><i></i><i></i><i></i></div>
    <div class="mark-faint" role="img" aria-label="Faint brand emblem decoration"></div>
    <div class="band"><span>481 Palomar Lane, Yellowknife, NT · (867) 555-0142</span><span>http://www.brightmeadowdogboarding.example</span></div>
  </section>

  <section class="sheet envelope" aria-label="Envelope back">
    <svg width="340" height="150" viewBox="0 0 340 150" aria-hidden="true">
      <path d="M0 0 L170 78 L340 0" fill="none" stroke="#d6d6d6" stroke-width="1.5"/>
    </svg>
    <div class="logo"><div class="brand-name"><span class="brand-dot"></span>Bright Meadow Dog Boarding</div></div>
  </section>

</body>
</html>
```